Realtor business card

Looking for a business card that will stand out from the rest. My area of expertise is residential real estate and loans.

Industry/Entity Type

Residential

Requirements
Must have
• Marcus Whitley, SFR
Broker
Mortgage Loan Originator
Notary Public
DRE License #07329184
NMLS 581706
Cell 714-552-0718
Fax 888-417-2965
www.marcuswhitleyhomes.example
mw@marcuswhitleyhomes.example

```html
<!DOCTYPE html>
<html lang="en">
<head>
<meta charset="utf-8">
<title>Marcus Whitley – Business Card</title>
<link rel="stylesheet" href="https://fonts.googleapis.com/css2?family=Carlito:wght@400;700&display=swap">
<style>
  :root {
    --card-green: #0d5f00;
    --text-green: #0d6b00;
    --white: #ffffff;
    --rule-grey: #8a8a8a;
    --icon-grey: #8c8c8c;
    --page: #ffffff;
  }
  html, body {
    margin: 0;
    padding: 0;
    width: 1200px;
    height: 777px;
    overflow: hidden;
    background: var(--page);
  }
  .card {
    position: relative;
    width: 1200px;
    height: 777px;
    background: var(--card-green);
    border-radius: 56px;
    overflow: hidden;
    font-family: "Carlito", "Calibri", sans-serif;
  }
  .name-tab {
    position: absolute;
    left: -4px;
    top: 118px;
    width: 684px;
    height: 122px;
    background: var(--white);
    border: 3px solid var(--rule-grey);
    border-left: none;
    border-radius: 0 62px 62px 0;
    box-sizing: border-box;
  }
  .name {
    position: absolute;
    left: 88px;
    top: 136px;
    margin: 0;
    font-size: 66px;
    font-weight: 400;
    line-height: 80px;
    color: var(--text-green);
    letter-spacing: 1px;
  }
  .credentials {
    position: absolute;
    right: 50px;
    top: 108px;
    margin: 0;
    padding: 0;
    list-style: none;
    text-align: right;
    color: var(--white);
    font-size: 64px;
    line-height: 72.5px;
    letter-spacing: 0.5px;
  }
  .contact-band {
    position: absolute;
    left: 0;
    top: 548px;
    width: 100%;
    height: 181px;
    background: var(--white);
    border-top: 5px solid var(--rule-grey);
    border-bottom: 5px solid var(--rule-grey);
    box-sizing: border-box;
  }
  .contact {
    position: absolute;
    display: flex;
    align-items: center;
    color: var(--text-green);
  }
  .contact svg { position: absolute; fill: var(--icon-grey); }
  .contact-phone, .contact-fax { font-size: 46px; }
  .contact-email, .contact-web { font-size: 37px; }
  .contact-phone { left: 176px; top: 566px; }
  .contact-fax   { left: 176px; top: 650px; }
  .contact-email { left: 620px; top: 572px; }
  .contact-web   { left: 620px; top: 656px; }
  .contact-phone svg { left: -106px; top: 4px; }
  .contact-fax svg   { left: -134px; top: 2px; }
  .contact-email svg { left: -92px; top: 4px; }
  .contact-web svg   { left: -94px; top: -4px; }
</style>
</head>
<body>
<div class="card">
  <div class="name-tab"></div>
  <h1 class="name">Marcus Whitley</h1>

  <ul class="credentials">
    <li>SFR</li>
    <li>Broker</li>
    <li>Mortgage Loan Originator</li>
    <li>Notary Public</li>
    <li>DRE License #07329184</li>
    <li>NMLS 581706</li>
  </ul>

  <div class="contact-band"></div>

  <div class="contact contact-phone">
    <svg width="30" height="54" viewBox="0 0 30 54" aria-hidden="true">
      <rect x="10" y="0" width="4" height="10" rx="2"/>
      <rect x="0" y="8" width="30" height="46" rx="7"/>
      <rect x="6" y="15" width="18" height="18" rx="2" fill="#ffffff"/>
    </svg>
    <span>714-552-0718</span>
  </div>

  <div class="contact contact-fax">
    <svg width="92" height="56" viewBox="0 0 92 56" aria-hidden="true">
      <rect x="0" y="18" width="14" height="38" rx="4"/>
      <rect x="18" y="18" width="74" height="38" rx="6"/>
      <rect x="34" y="0" width="40" height="30" rx="2"/>
      <rect x="40" y="7" width="20" height="3" fill="#ffffff"/>
      <rect x="40" y="14" width="28" height="3" fill="#ffffff"/>
      <rect x="40" y="21" width="28" height="3" fill="#ffffff"/>
    </svg>
    <span>888-417-2965</span>
  </div>

  <div class="contact contact-email">
    <svg width="58" height="40" viewBox="0 0 58 40" aria-hidden="true">
      <rect x="0" y="0" width="58" height="40" rx="6"/>
      <path d="M6 6 L29 22 L52 6 M6 34 L22 19 M52 34 L36 19" stroke="#ffffff" stroke-width="5" fill="none" stroke-linecap="round"/>
    </svg>
    <span>mw@marcuswhitleyhomes.example</span>
  </div>

  <div class="contact contact-web">
    <svg width="62" height="58" viewBox="0 0 62 58" aria-hidden="true">
      <path d="M31 0 L62 27 L56 32 L31 10 L6 32 L0 27 Z"/>
      <rect x="44" y="4" width="8" height="14"/>
      <path d="M10 31 L31 13 L52 31 V58 H37 V40 H25 V58 H10 Z"/>
    </svg>
    <span>www.marcuswhitleyhomes.example</span>
  </div>
</div>
</body>
</html>
```